Need a sleek, professional business card design for a Web Development business

I need a unique business card designed for a web development company. It is also the parent company for any ventures I do, such as my ClipWave channel, startup ideas I have, etc. I am the single member of "Bright Harbor Code LLC." I will attach my basic logo here, so you will see the current color scheme and have the asset available. Thank you!

Target Market(s)

Startups, SMB's, Professionals

Industry/Entity Type

Business

Font styles to use
Other font styles liked:
• Lovello for headings is what I use, but not necessary.

Colors

Designer to choose colors to be used in the design.

Requirements
Nice to have
• Sleek is the word. Professional, modern, dark.
Should not have
• Any work from someone else's design. Lacking originality.

```html
<!DOCTYPE html>
<html lang="en">
<head>
<meta charset="utf-8">
<title>Bright Harbor Code LLC — Business Card</title>
<link rel="stylesheet" href="https://fonts.googleapis.com/css2?family=Roboto:wght@400;500;700&display=swap">
<style>
  :root {
    --stage: #ece8e4;
    --card-white: #fbfaf9;
    --coral: #ee5a6f;
    --coral-soft: #f06b72;
    --peach: #f6955e;
    --ink: #2b2b2b;
    --ink-soft: #3a3a3a;
    --tile: #333333;
  }
  * { box-sizing: border-box; margin: 0; padding: 0; }
  html, body { width: 1200px; height: 911px; overflow: hidden; }
  body {
    background: var(--stage);
    font-family: "Roboto", Arial, sans-serif;
    position: relative;
  }

  /* Front card */
  .card-front {
    position: absolute;
    left: 110px; top: 123px;
    width: 380px; height: 665px;
    background: var(--card-white);
    border: 8px solid var(--coral);
    border-radius: 22px;
    box-shadow: 0 14px 30px rgba(0,0,0,.18);
  }
  .brand-tile {
    position: absolute;
    left: 95px; top: 60px;
    width: 174px; height: 174px;
    background: var(--tile);
    border-radius: 14px;
  }
  .brand-name {
    position: absolute;
    left: 0; right: 0; top: 262px;
    text-align: center;
    font-weight: 700;
    font-size: 25px;
    color: var(--ink);
  }
  .contact {
    position: absolute;
    left: 38px; top: 370px;
    display: flex;
  }
  .contact-icons {
    display: flex; flex-direction: column; gap: 26px;
    padding-top: 2px; width: 30px; align-items: center;
  }
  .contact-icons svg { width: 16px; height: 16px; fill: var(--coral); }
  .contact-rule {
    width: 2px; background: var(--ink); margin: 0 16px 0 8px;
  }
  .contact-text { color: var(--ink-soft); font-size: 17px; line-height: 22px; }
  .person-name {
    color: var(--coral);
    font-weight: 500;
    font-size: 22px;
    letter-spacing: .5px;
    line-height: 26px;
  }
  .person-role { font-size: 18px; letter-spacing: .5px; margin-bottom: 4px; }

  /* Back card */
  .card-back {
    position: absolute;
    left: 560px; top: 300px;
    width: 580px; height: 345px;
    border: 8px solid var(--tile);
    border-radius: 22px;
    background: radial-gradient(ellipse at 55% 50%, var(--peach) 0%, var(--coral-soft) 70%, var(--coral) 100%);
    box-shadow: 0 14px 30px rgba(0,0,0,.22);
  }
  .back-url {
    position: absolute;
    left: 38px; top: 50%;
    transform: translate(-50%, -50%) rotate(90deg);
    transform-origin: center;
    margin-left: 10px;
    font-size: 13px;
    letter-spacing: 5px;
    color: var(--ink);
    white-space: nowrap;
  }
  .back-brand {
    position: absolute;
    left: 60px; right: 0; top: 50%;
    transform: translateY(-50%);
    display: flex; flex-direction: column; align-items: center; gap: 18px;
  }
  .back-mark {
    width: 70px; height: 70px; border-radius: 50%; background: var(--tile);
  }
  .back-brand-name {
    font-weight: 700; font-size: 28px; color: var(--tile);
  }
</style>
</head>
<body>

<section class="card-front">
  <div class="brand-tile"></div>
  <div class="brand-name">Bright Harbor Code LLC.</div>

  <div class="contact">
    <div class="contact-icons">
      <svg viewBox="0 0 16 16" aria-label="Name"><circle cx="8" cy="5" r="3.5"/><path d="M1 16c0-4 3-6 7-6s7 2 7 6z"/></svg>
      <svg viewBox="0 0 16 16" aria-label="Address"><path d="M8 0a5.5 5.5 0 0 0-5.5 5.5C2.5 10 8 16 8 16s5.5-6 5.5-10.5A5.5 5.5 0 0 0 8 0zm0 8a2.5 2.5 0 1 1 0-5 2.5 2.5 0 0 1 0 5z"/></svg>
      <svg viewBox="0 0 16 16" aria-label="Phone"><path d="M3 1l3 3-1.5 2a9 9 0 0 0 5.5 5.5L12 10l3 3-2 2C6 15 1 10 1 3z"/></svg>
      <svg viewBox="0 0 16 16" aria-label="Mobile"><path d="M4 0h8a1 1 0 0 1 1 1v14a1 1 0 0 1-1 1H4a1 1 0 0 1-1-1V1a1 1 0 0 1 1-1zm1 2v10h6V2z"/></svg>
      <svg viewBox="0 0 16 16" aria-label="Email"><path d="M0 3h16v10H0zm1.5 1.2L8 9l6.5-4.8V4h-13z"/></svg>
      <svg viewBox="0 0 16 16" aria-label="Website"><circle cx="8" cy="8" r="7.5"/><path d="M1 8h14M8 .5c3 3 3 12 0 15M8 .5c-3 3-3 12 0 15" stroke="#fbfaf9" stroke-width="1.2" fill="none"/></svg>
    </div>
    <div class="contact-rule"></div>
    <div class="contact-text">
      <div class="person-name">ALEX MARLOW</div>
      <div class="person-role">CEO/FOUNDER</div>
      <div>4120 Cedar Bend Road</div>
      <div>Fairbanks, Alaska 99701</div>
      <div>555 214 7702</div>
      <div>555 381 6045</div>
      <div>555 907 3318</div>
      <div>alex@brightharborcode.com</div>
      <div>www.brightharborcode.com</div>
    </div>
  </div>
</section>

<section class="card-back">
  <div class="back-url">www.brightharborcode.com</div>
  <div class="back-brand">
    <div class="back-mark"></div>
    <div class="back-brand-name">Bright Harbor Code LLC</div>
  </div>
</section>

</body>
</html>
```